Financial Planning Pyramid Graphic

I need a graphic of a pyramid including 3 levels.

I've attached a copy of the article to be published with the graphic.

Also attached company logos if it makes sense to use.

See www.NovalisCapitalAdvisors.com for a general reference.

Target Market(s)

small and medium size business owners who intend to eventually sell their business. primarily servicing the construction, real estate, and technology industries.

Industry/Entity Type

Financial Planning

Font styles to use
Sans Serif

Requirements
Must have
• Primary branding hex color #009b81

Three levels of the pyramid:
3. Top: Wealth Distribution
2. Middle: Growing Wealth
1. Base: Protection (Risk Management)

It should somehow show how "Tax Planning" permeates all 3 layers.
Nice to have
• The attached article includes details about what the graphic should represent and more details that may be included.

```html
<!DOCTYPE html>
<html lang="en">
<head>
<meta charset="utf-8">
<title>Financial Planning Pyramid</title>
<link href="https://fonts.googleapis.com/css2?family=Barlow+Condensed:wght@500;600;700&display=swap" rel="stylesheet">
<style>
  :root {
    --page: #e9e9e9;
    --card: #ffffff;
    --arrow: #58595b;
    --teal: #009b81;
    --teal-light: #00a79d;
    --teal-dark: #008c7c;
    --lime: #cbe44e;
    --lime-side: #b4c844;
    --lime-ledge: #a4ac2f;
    --lime-text: #b2c43d;
    --navy: #22526f;
    --navy-side: #1f4763;
    --navy-ledge: #163a52;
    --navy-text: #234e6e;
    --white: #ffffff;
  }
  html, body {
    margin: 0;
    padding: 0;
    width: 1200px;
    height: 824px;
    overflow: hidden;
    background: var(--page);
  }
  .pyramid-graphic {
    display: block;
    width: 1200px;
    height: 824px;
  }
  .label {
    font-family: "Barlow Condensed", sans-serif;
    font-weight: 600;
    font-size: 58px;
  }
  .label--distribution { fill: var(--teal); }
  .label--growing { fill: var(--lime-text); }
  .label--protection { fill: var(--navy-text); }
  .arrow-text {
    font-family: "Barlow Condensed", sans-serif;
    font-weight: 700;
    font-size: 52px;
    fill: var(--white);
    letter-spacing: 1px;
  }
  .tier-number {
    font-family: "Barlow Condensed", sans-serif;
    font-weight: 700;
    font-size: 86px;
    fill: var(--white);
  }
  .icon {
    fill: none;
    stroke: var(--white);
    stroke-width: 4;
    stroke-linecap: round;
    stroke-linejoin: round;
  }
  .icon-text {
    font-family: "Barlow Condensed", sans-serif;
    font-weight: 700;
    font-size: 22px;
    fill: var(--white);
  }
</style>
</head>
<body>
<svg class="pyramid-graphic" viewBox="0 0 1640 1126" xmlns="http://www.w3.org/2000/svg">
  <rect class="card" x="100" y="105" width="1440" height="915" fill="var(--card)"/>

  <!-- Tax planning arrow -->
  <g class="tax-arrow">
    <polygon points="281,192 364,312 321,312 321,740 240,740 240,312 198,312" fill="var(--arrow)"/>
    <text class="arrow-text" transform="translate(300,478) rotate(-90)" text-anchor="middle">TAX PLANNING</text>
  </g>

  <!-- Base tier -->
  <g class="tier tier--protection">
    <polygon points="352,588 581,455 808,588 581,725" fill="var(--navy-ledge)"/>
    <polygon points="240,725 581,933 581,722 352,588" fill="var(--navy)"/>
    <polygon points="922,725 581,933 581,722 808,588" fill="var(--navy-side)"/>
    <text class="tier-number" transform="translate(402,788) skewY(30)">1</text>
    <g class="icon">
      <path d="M716,666 l30,14 v28 c0,22 -14,38 -30,46 c-16,-8 -30,-24 -30,-46 v-28 z"/>
      <path d="M702,712 l10,10 l20,-22"/>
      <path d="M680,740 v40 l24,24 v16 M752,730 v40 l-24,24 v16"/>
    </g>
  </g>

  <!-- Middle tier -->
  <g class="tier tier--growing">
    <polygon points="467,402 581,340 694,402 581,458" fill="var(--lime-ledge)"/>
    <polygon points="352,552 581,692 581,458 467,418" fill="var(--lime)"/>
    <polygon points="808,552 581,692 581,458 694,418" fill="var(--lime-side)"/>
    <text class="tier-number" transform="translate(470,560) skewY(30)">2</text>
    <g class="icon">
      <circle cx="680" cy="496" r="15"/>
      <path d="M680,512 v56 M680,540 c-10,-12 -28,-10 -32,4 c14,4 26,2 32,-4 M680,530 c8,-12 24,-14 30,-2 c-12,6 -24,6 -30,2"/>
      <path d="M628,620 v-34 l22,-4 l30,10 h20 l26,-34 M650,600 l50,-14"/>
    </g>
    <text class="icon-text" x="680" y="504" text-anchor="middle">$</text>
  </g>

  <!-- Top tier -->
  <g class="tier tier--distribution">
    <polygon points="581,251 467,390 581,460" fill="var(--teal-light)"/>
    <polygon points="581,251 694,390 581,460" fill="var(--teal-dark)"/>
    <text class="tier-number" transform="translate(510,352) rotate(90) scale(0.8)">3</text>
    <g class="icon">
      <circle cx="625" cy="356" r="13"/>
      <path d="M592,388 l-4,-12 l22,-10 l22,8 l20,-12 M606,398 l50,-22"/>
    </g>
    <text class="icon-text" x="625" y="364" text-anchor="middle">$</text>
  </g>

  <!-- Leaders and labels -->
  <g class="leader leader--distribution" stroke="var(--teal)" stroke-width="4" fill="none">
    <polyline points="648,330 717,288 815,288"/>
  </g>
  <circle cx="816" cy="288" r="11" fill="var(--teal)"/>
  <text class="label label--distribution" x="855" y="304">Wealth Distribution</text>

  <g class="leader leader--growing" stroke="var(--lime-text)" stroke-width="4" fill="none">
    <polyline points="755,485 805,452 903,452"/>
  </g>
  <circle cx="904" cy="452" r="11" fill="var(--lime-text)"/>
  <text class="label label--growing" x="960" y="470">Growing Wealth</text>

  <g class="leader leader--protection" stroke="var(--navy-text)" stroke-width="4" fill="none">
    <polyline points="795,703 910,633 1008,633"/>
  </g>
  <circle cx="1009" cy="633" r="11" fill="var(--navy-text)"/>
  <text class="label label--protection" x="1058" y="626">Protection</text>
  <text class="label label--protection" x="1058" y="692">(Risk Management)</text>
</svg>
</body>
</html>
```